Travel Agency Website - Simple General

Need a 7 page simple design that is pretty repetitive. Need to be able to load quickly that is SEO optimized. Trying to give ideas on what they can do, be personal as we are local, but at the same time come across as professional and get information easily with little burden.

- Landing Page
- Brambleton Vacations Page
- Family Trips
- Road Trips from Texas
- Other Destinations
- About Us Page
- Contact Us Page

Target Market(s)

Families

Coding

Coded - Design and coding required

Number of Pages Required

5+ page

Colors

Designer to choose colors to be used in the design.

Requirements
Must have
• Like it to flow easily with our logo. Use that for colors, etc.

```html
<!DOCTYPE html>
<html lang="en">
<head>
<meta charset="utf-8">
<title>Meadowlark Journeys – Travel Co.</title>
<link href="https://fonts.googleapis.com/css2?family=Montserrat:wght@500;600;700&family=Jost:wght@400;500&family=Parisienne&display=swap" rel="stylesheet">
<style>
:root{
  --teal:#1f9aa3;
  --gold:#c08a35;
  --ink:#0b2930;
  --white:#ffffff;
  --muted:#a9b9bc;
  --rule:#2c4a51;
}
*{box-sizing:border-box;margin:0;padding:0}
html,body{width:886px;height:1200px;overflow:hidden;background:var(--white)}
body{position:relative;font-family:"Jost",sans-serif;color:var(--white)}
.hero{position:absolute;left:0;top:0;width:886px;height:534px;
  background:linear-gradient(180deg,#5f7f9c 0%,#7d93a6 18%,#4f6b5a 36%,#1f7d7c 52%,#167070 70%,#0f5a5c 100%);}
.hero-scene{position:absolute;inset:0;
  background:radial-gradient(ellipse 140px 200px at 600px 330px,rgba(190,60,110,.75),rgba(190,60,110,0) 100%),
             radial-gradient(ellipse 170px 300px at 120px 200px,rgba(120,100,80,.6),rgba(0,0,0,0)),
             radial-gradient(ellipse 150px 260px at 450px 150px,rgba(110,95,75,.5),rgba(0,0,0,0)),
             linear-gradient(160deg,rgba(0,0,0,0) 70%,rgba(140,80,50,.55) 90%);}
.topbar{position:absolute;left:0;top:0;width:886px;height:32px;background:rgba(40,50,60,.35);
  display:flex;justify-content:space-between;align-items:center;padding:0 63px;font-size:11px}
.topbar .item{display:flex;align-items:center;gap:6px}
.dot{width:16px;height:16px;border-radius:50%;background:var(--gold);display:flex;align-items:center;justify-content:center;flex:none}
.brand{position:absolute;display:flex;align-items:center;gap:8px}
.brand .disc{width:20px;height:20px;border-radius:50%;background:var(--gold)}
.brand span{font-family:"Montserrat",sans-serif;font-weight:700;font-size:14px;line-height:1.1;color:var(--white)}
.nav{position:absolute;right:64px;top:79px;display:flex;gap:28px;font-family:"Montserrat",sans-serif;font-weight:600;font-size:10.5px;letter-spacing:.6px}
.nav a{color:var(--white);text-decoration:none}
.nav a.active{color:var(--teal)}
.hero-title{position:absolute;left:64px;top:168px;font-family:"Parisienne",cursive;font-size:74px;line-height:72px;color:var(--white);font-weight:400}
.btn{position:absolute;left:64px;top:350px;width:127px;height:35px;border-radius:18px;background:var(--gold);
  display:flex;align-items:center;justify-content:center;gap:5px;font-family:"Montserrat",sans-serif;font-weight:600;font-size:9.5px;letter-spacing:1.2px;color:var(--white)}
.cards{position:absolute;top:596px;left:63px;display:flex;gap:29px}
.card{position:relative;width:168px;height:247px}
.card .label{position:absolute;left:0;bottom:0;width:100%;height:50px;background:rgba(40,40,40,.55);
  display:flex;flex-direction:column;align-items:center;justify-content:center;font-family:"Montserrat",sans-serif;font-weight:700;font-size:11.5px;letter-spacing:.8px;text-align:center;white-space:nowrap}
.card .label.tight{font-size:10.5px;letter-spacing:.4px}
.card .label small{font-weight:500;font-size:10px;letter-spacing:.6px}
.c1{background:linear-gradient(180deg,#f1d2bd,#c9504a 55%,#6a7fb3)}
.c2{background:linear-gradient(180deg,#5f8a78,#9a8a6a 50%,#d59a4a)}
.c3{background:linear-gradient(180deg,#6f7a6a,#c7b9a5 45%,#6f8aa8)}
.c4{background:linear-gradient(180deg,#c9dce9,#8fa5b5 40%,#2f4a3e)}
.footer{position:absolute;left:0;top:902px;width:886px;height:298px;background:var(--ink)}
.col-title{position:absolute;top:75px;font-family:"Montserrat",sans-serif;font-weight:600;font-size:10.5px;letter-spacing:1px}
.links{position:absolute;left:282px;top:105px;list-style:none;font-size:10.5px;color:var(--muted)}
.links li{height:25.5px}
.contact{position:absolute;left:474px;top:100px;font-size:10.5px;color:var(--muted)}
.contact .row{display:flex;align-items:center;gap:7px;height:31px}
.social{position:absolute;right:63px;top:102px;display:flex;gap:5px}
.social .s{width:25px;height:25px;border-radius:50%;background:var(--white);display:flex;align-items:center;justify-content:center}
.bottom{position:absolute;left:63px;right:63px;top:258px;display:flex;align-items:center;gap:8px;font-size:9.5px;color:var(--muted)}
.bottom .line{flex:1;height:1px;background:var(--rule)}
.bottom b{font-weight:400;color:var(--gold)}
</style>
</head>
<body>
<header class="hero">
  <div class="hero-scene" role="img" aria-label="Traveller in a flowing pink dress at the bow of a wooden boat among limestone cliffs and turquoise water"></div>
  <div class="topbar">
    <div class="item"><span class="dot"><svg width="8" height="8" viewBox="0 0 24 24"><path fill="#fff" d="M6.6 10.8a15 15 0 006.6 6.6l2.2-2.2a1 1 0 011-.25 11.4 11.4 0 003.6.57 1 1 0 011 1V20a1 1 0 01-1 1A17 17 0 013 4a1 1 0 011-1h3.5a1 1 0 011 1 11.4 11.4 0 00.57 3.6 1 1 0 01-.25 1z"/></svg></span>555-014-2237</div>
    <div class="item"><span class="dot"><svg width="8" height="8" viewBox="0 0 24 24"><path fill="#fff" d="M3 5h18v14H3z"/><path fill="none" stroke="#c08a35" stroke-width="2" d="M3 6l9 7 9-7"/></svg></span>hello@meadowlarkjourneys.com</div>
  </div>
  <div class="brand" style="left:65px;top:62px"><div class="disc"></div><span>Meadowlark<br>Journeys</span></div>
  <nav class="nav">
    <a class="active" href="#">HOME</a>
    <a href="#">BRAMBLETON VACATIONS</a>
    <a href="#">ABOUT US</a>
    <a href="#">CONTACT US</a>
  </nav>
  <h1 class="hero-title">Meadowlark<br>Journeys</h1>
  <a class="btn">CONTACT US <svg width="9" height="9" viewBox="0 0 24 24"><circle cx="12" cy="12" r="11" fill="#fff"/><path d="M9 7l5 5-5 5" stroke="#c08a35" stroke-width="3" fill="none"/></svg></a>
</header>

<section class="cards">
  <div class="card c1" role="img" aria-label="Colourful castle-style resort with fountains"><div class="label tight">BRAMBLETON VACATIONS<small>LAND AND SEA</small></div></div>
  <div class="card c2" role="img" aria-label="Family cheering with arms raised on a hillside"><div class="label">FAMILY TRIPS</div></div>
  <div class="card c3" role="img" aria-label="Friends reading a map beside an off-road vehicle"><div class="label">TEXAS ROAD TRIPS</div></div>
  <div class="card c4" role="img" aria-label="Hiker in a knit hat overlooking a mountain lake"><div class="label">OTHER DESTINATIONS</div></div>
</section>

<footer class="footer">
  <div class="brand" style="left:65px;top:95px"><div class="disc"></div><span>Meadowlark<br>Journeys</span></div>
  <div class="col-title" style="left:282px">QUICK LINKS</div>
  <ul class="links"><li>Home</li><li>Brambleton Vacations</li><li>About Us</li><li>Contact Us</li></ul>
  <div class="col-title" style="left:474px">CONTACT INFO</div>
  <div class="contact">
    <div class="row"><span class="dot"><svg width="8" height="8" viewBox="0 0 24 24"><path fill="#fff" d="M6.6 10.8a15 15 0 006.6 6.6l2.2-2.2a1 1 0 011-.25 11.4 11.4 0 003.6.57 1 1 0 011 1V20a1 1 0 01-1 1A17 17 0 013 4a1 1 0 011-1h3.5a1 1 0 011 1 11.4 11.4 0 00.57 3.6 1 1 0 01-.25 1z"/></svg></span>555-014-2237</div>
    <div class="row"><span class="dot"><svg width="8" height="8" viewBox="0 0 24 24"><path fill="#fff" d="M3 5h18v14H3z"/><path fill="none" stroke="#c08a35" stroke-width="2" d="M3 6l9 7 9-7"/></svg></span>hello@meadowlarkjourneys.com</div>
  </div>
  <div class="col-title" style="right:63px">FOLLOW US</div>
  <div class="social">
    <span class="s" aria-label="Share"><svg width="11" height="11" viewBox="0 0 24 24"><g fill="#1f9aa3"><circle cx="18" cy="5" r="3"/><circle cx="6" cy="12" r="3"/><circle cx="18" cy="19" r="3"/></g><path d="M18 5L6 12l12 7" stroke="#1f9aa3" stroke-width="2" fill="none"/></svg></span>
    <span class="s" aria-label="Link"><svg width="11" height="11" viewBox="0 0 24 24"><path d="M10 14a4 4 0 005.7 0l3-3a4 4 0 00-5.7-5.7l-1 1M14 10a4 4 0 00-5.7 0l-3 3a4 4 0 005.7 5.7l1-1" stroke="#1f9aa3" stroke-width="2.2" fill="none" stroke-linecap="round"/></svg></span>
  </div>
  <div class="bottom"><span>© 2026 <b>Meadowlark Journeys</b>. All right reserved.</span><span class="line"></span><span>May 06, 2026. Layout_4</span></div>
</footer>
</body>
</html>
```